Tallowmere Consulting Group Business Card Design

We have the logo we just need someone to design a modern business card design.

Name: Leopold Ganzhurt
Phone: 3052918364
Mobile: 9178402297
Web:www.tallowmereconsulting.com
email: lganzhurt@tallowmereconsulting.com
Company: Tallowmere Consulting Group
Title: CEO

Address: 718 Quenby Ave, Miami, Florida 33187

Target Market(s)

companies over 100 employees

Industry/Entity Type

Business

```html
<!DOCTYPE html>
<html lang="en">
<head>
<meta charset="utf-8">
<title>Tallowmere Consulting Group – Business Card</title>
<link href="https://fonts.googleapis.com/css2?family=Arimo:wght@400;700&display=swap" rel="stylesheet">
<style>
  :root {
    --brand-blue: #3a78dd;
    --card-white: #f4f3f2;
    --ink: #2b2b2b;
    --ink-soft: #3d3d3d;
    --backdrop: #d9d6d5;
  }
  * { box-sizing: border-box; margin: 0; padding: 0; }
  html, body {
    width: 1200px; height: 1000px; overflow: hidden;
    background: var(--backdrop);
    font-family: "Arimo", Arial, sans-serif;
  }
  .canvas {
    position: relative; width: 1200px; height: 1000px;
  }
  .card {
    position: absolute; left: 250px; width: 700px; height: 400px;
    overflow: hidden;
    box-shadow: 0 6px 18px rgba(0,0,0,0.12);
  }
  /* Front side */
  .card-front { top: 60px; background: var(--brand-blue); color: #fff; }
  .front-lockup {
    position: absolute; left: 0; right: 0; top: 118px;
    display: flex; flex-direction: column; align-items: center;
  }
  .front-lockup .brand-dot {
    width: 76px; height: 76px; border-radius: 50%; background: #fff;
    margin-bottom: 18px;
  }
  .front-lockup .brand-name {
    font-weight: 700; font-size: 40px; letter-spacing: 2px; line-height: 1;
  }
  .front-lockup .brand-sub {
    font-weight: 400; font-size: 12px; letter-spacing: 2px; margin-top: 6px;
  }
  /* Back side */
  .card-back { top: 540px; background: var(--card-white); color: var(--ink); }
  .back-lockup {
    position: absolute; right: 40px; top: 30px;
    display: flex; flex-direction: column; align-items: flex-end;
  }
  .back-lockup .brand-dot {
    width: 46px; height: 46px; border-radius: 50%; background: var(--brand-blue);
    margin-bottom: 8px; margin-right: 70px;
  }
  .back-lockup .brand-name {
    font-weight: 700; font-size: 24px; letter-spacing: 1px; line-height: 1;
  }
  .back-lockup .brand-sub {
    font-size: 8px; letter-spacing: 1.5px; margin-top: 3px; color: var(--ink-soft);
  }
  .address {
    position: absolute; right: 40px; top: 130px; text-align: right;
    font-size: 15px; line-height: 1.35; color: var(--ink-soft);
  }
  .contact {
    position: absolute; right: 40px; top: 210px; text-align: right;
    font-size: 15px; line-height: 1.4; color: var(--ink-soft);
  }
  .contact b { font-weight: 700; color: var(--ink); }
  .contact .web { margin-top: 0; }
  .person {
    position: absolute; left: 40px; top: 200px;
  }
  .person .name { font-size: 22px; color: var(--ink); }
  .person .name b { font-weight: 700; }
  .person .title { font-size: 15px; margin-top: 4px; color: var(--ink-soft); }
  .deco-circle {
    position: absolute; left: 20px; top: 280px;
    width: 300px; height: 300px; border-radius: 50%;
    background: var(--brand-blue);
  }
</style>
</head>
<body>
<main class="canvas">
  <section class="card card-front" aria-label="Card front">
    <div class="front-lockup">
      <span class="brand-dot"></span>
      <span class="brand-name">TALLOWMERE</span>
      <span class="brand-sub">CONSULTING GROUP</span>
    </div>
  </section>

  <section class="card card-back" aria-label="Card back">
    <div class="deco-circle"></div>
    <div class="back-lockup">
      <span class="brand-dot"></span>
      <span class="brand-name">TALLOWMERE</span>
      <span class="brand-sub">CONSULTING GROUP</span>
    </div>
    <p class="address">718 Quenby Ave,<br>Miami, Florida 33187</p>
    <div class="person">
      <p class="name"><b>Leopold</b>Ganzhurt</p>
      <p class="title">CEO</p>
    </div>
    <div class="contact">
      <p><b>T</b> : 3052918364</p>
      <p><b>M</b> : 9178402297</p>
      <p><b>E</b> : lganzhurt@tallowmereconsulting.com</p>
      <p class="web">www.<b>tallowmereconsulting</b>.com</p>
    </div>
  </section>
</main>
</body>
</html>
```